BrackenQuayCards
Business Cards
BrackenQuayCards - Law
Creative Brief
Professional
Matthias Lowe
Publisher
4751 Henley Court, Juniper Business Pavilion, 2nd Floor, Harlow Bay, Westmere, 92417-3051
lowe@brackenquay.example
www.brackenquay.example
Need delivery as AI file. Must be able to edit to add names, contact info, etc.

```html
<!DOCTYPE html>
<html lang="en">
<head>
<meta charset="utf-8">
<title>BrackenQuayCards – Business Card</title>
<link href="https://fonts.googleapis.com/css2?family=Open+Sans:wght@400;600;700&display=swap" rel="stylesheet">
<style>
  :root {
    --page: #eceeef;
    --card: #ffffff;
    --ink: #1a1a1a;
    --gold-light: #e9cd6e;
    --gold: #cfa83f;
    --gold-deep: #b38a27;
    --soft-grey: #c9cbcd;
    --mid-grey: #6d6f71;
  }
  * { margin: 0; padding: 0; box-sizing: border-box; }
  html, body {
    width: 1200px; height: 1009px; overflow: hidden;
    background: var(--page);
    font-family: "Open Sans", Arial, sans-serif;
  }
  .canvas { position: relative; width: 1200px; height: 1009px; }

  .card {
    position: absolute;
    width: 760px; height: 434px;
    border-radius: 24px;
    background: var(--card);
    overflow: hidden;
    box-shadow: 0 6px 18px rgba(0,0,0,0.12);
  }
  .card-back { left: 380px; top: 50px; }
  .card-front { left: 60px; top: 530px; }

  /* back side */
  .back-mark {
    position: absolute; left: 0; right: 0; top: 150px;
    display: flex; justify-content: center; align-items: center; gap: 10px;
    color: var(--soft-grey); font-weight: 700; font-size: 40px; letter-spacing: 0.5px;
  }
  .back-mark .dot {
    width: 14px; height: 14px; border-radius: 50%; background: var(--soft-grey);
  }
  .back-url {
    position: absolute; left: 0; right: 0; top: 236px; text-align: center;
    color: var(--mid-grey); font-size: 14px; letter-spacing: 3px;
  }

  /* front side */
  .card-art { position: absolute; inset: 0; }
  .brand { position: absolute; left: 330px; top: 70px; }
  .brand-name {
    display: flex; align-items: center; gap: 10px;
    color: var(--ink); font-weight: 700; font-size: 30px; line-height: 1;
  }
  .brand-name .dot {
    width: 12px; height: 12px; border-radius: 50%; background: var(--ink);
  }
  .brand-tagline {
    margin-top: 6px; color: var(--ink); font-size: 11px; font-weight: 600; letter-spacing: 0.2px;
  }
  .contact {
    position: absolute; left: 30px; top: 232px;
    list-style: none; color: #fff; font-size: 12px; line-height: 20px;
  }
  .contact li { display: flex; align-items: center; gap: 8px; }
  .contact svg { width: 12px; height: 12px; flex: none; }
  .person {
    position: absolute; right: 36px; bottom: 26px; text-align: right; color: #fff;
  }
  .person-name { font-size: 22px; font-weight: 700; line-height: 1.2; }
  .person-role { font-size: 14px; font-weight: 400; }
</style>
</head>
<body>
<main class="canvas">

  <section class="card card-back" aria-label="Business card back">
    <div class="back-mark"><span class="dot"></span>Bracken Quay Investor</div>
    <p class="back-url">www.brackenquay.example</p>
  </section>

  <section class="card card-front" aria-label="Business card front">
    <svg class="card-art" viewBox="0 0 760 434" width="760" height="434" aria-hidden="true">
      <defs>
        <linearGradient id="goldFill" x1="0" y1="0" x2="1" y2="1">
          <stop offset="0" stop-color="#e9cd6e"/>
          <stop offset="0.5" stop-color="#cfa83f"/>
          <stop offset="1" stop-color="#b38a27"/>
        </linearGradient>
      </defs>
      <path d="M0,140 C220,160 500,270 760,328 L760,434 L0,434 Z" fill="url(#goldFill)"/>
      <path d="M-10,128 C220,148 500,258 770,318" fill="none" stroke="#1a1a1a" stroke-width="22"/>
      <path d="M-10,106 C220,126 500,236 770,296" fill="none" stroke="#cfa83f" stroke-width="4"/>
    </svg>

    <div class="brand">
      <div class="brand-name"><span class="dot"></span>Bracken Quay Investor</div>
      <p class="brand-tagline">Clear Counsel and Steady Guidance for the Careful Investor</p>
    </div>

    <ul class="contact">
      <li><svg viewBox="0 0 12 12"><path d="M6 0.5a3.8 3.8 0 0 0-3.8 3.8C2.2 7.2 6 11.5 6 11.5s3.8-4.3 3.8-7.2A3.8 3.8 0 0 0 6 0.5zm0 5.2a1.4 1.4 0 1 1 0-2.8 1.4 1.4 0 0 1 0 2.8z" fill="#fff"/></svg>4751 Henley Court, Juniper Business Pavilion</li>
      <li><svg viewBox="0 0 12 12"><circle cx="6" cy="6" r="2" fill="#fff"/></svg>2nd Floor, Harlow Bay, Westmere 92417-3051</li>
      <li><svg viewBox="0 0 12 12"><path d="M3 0.8l2 2.6-1.2 1.4c.7 1.5 1.9 2.7 3.4 3.4l1.4-1.2 2.6 2-1.2 2.2C5 11 1 7 0.8 2z" fill="#fff"/></svg>Tel +1 555 014 2283</li>
      <li><svg viewBox="0 0 12 12"><rect x="1.5" y="3" width="9" height="7" fill="#fff"/><rect x="3" y="0.8" width="6" height="3" fill="#fff"/></svg>Fax +1 555 014 2290</li>
      <li><svg viewBox="0 0 12 12"><rect x="0.8" y="2.2" width="10.4" height="7.6" fill="none" stroke="#fff" stroke-width="1.2"/><path d="M1 2.5 6 6.5 11 2.5" fill="none" stroke="#fff" stroke-width="1.2"/></svg>lowe@brackenquay.example</li>
      <li><svg viewBox="0 0 12 12"><circle cx="6" cy="6" r="5" fill="none" stroke="#fff" stroke-width="1.2"/><path d="M1 6h10M6 1c2 2.5 2 7.5 0 10M6 1c-2 2.5-2 7.5 0 10" fill="none" stroke="#fff" stroke-width="1"/></svg>www.brackenquay.example</li>
    </ul>

    <div class="person">
      <p class="person-name">Matthias Lowe</p>
      <p class="person-role">Publisher</p>
    </div>
  </section>

</main>
</body>
</html>
```